business card for trucking industry consulting firm

Our company, Velkor Services Inc. provides numerous services to the trucking industry as listed on our website: velkor.ca
The logo i want on the card is the black and red VELKOR
update: i would like the services we provide listed on the card (see velkor.ca)

```html
<!DOCTYPE html>
<html lang="en">
<head>
<meta charset="utf-8">
<title>Velkor Services Inc. — Business Card</title>
<link href="https://fonts.googleapis.com/css2?family=Montserrat:wght@400;500;700&family=Source+Sans+3:wght@400;600&display=swap" rel="stylesheet">
<style>
  :root {
    --backdrop: #d8d9db;
    --card: #ffffff;
    --ink: #1a1416;
    --red: #cc1f27;
    --muted: #3a3a3a;
  }
  * { margin: 0; padding: 0; box-sizing: border-box; }
  html, body { width: 800px; height: 1200px; overflow: hidden; }
  body {
    position: relative;
    background: var(--backdrop);
    font-family: "Montserrat", sans-serif;
    color: var(--ink);
  }
  .card {
    position: absolute;
    left: 148px;
    width: 504px;
    height: 288px;
    background: var(--card);
    overflow: hidden;
  }
  .card--front { top: 174px; }
  .card--back { top: 703px; }

  .brand {
    position: absolute;
    left: 0; right: 0;
    display: flex;
    align-items: center;
    justify-content: center;
    gap: 9px;
  }
  .brand__mark { width: 12px; height: 12px; background: var(--red); }
  .brand__name {
    font-family: "Montserrat", sans-serif;
    font-weight: 700;
    color: var(--ink);
    letter-spacing: 0.5px;
    line-height: 1;
  }
  .card--front .brand { top: 66px; }
  .card--front .brand__name { font-size: 19px; }
  .card--back .brand { top: 86px; }
  .card--back .brand__name { font-size: 22px; }
  .card--back .brand__mark { width: 14px; height: 14px; }

  .person {
    position: absolute;
    right: 262px;
    top: 180px;
    text-align: right;
  }
  .person__name { font-size: 24px; font-weight: 500; line-height: 1; }
  .person__role { font-size: 12px; color: var(--muted); margin-top: 4px; }

  .divider {
    position: absolute;
    left: 252px;
    top: 158px;
    width: 1px;
    height: 89px;
    background: var(--ink);
  }

  .contacts {
    position: absolute;
    left: 267px;
    top: 161px;
    list-style: none;
    font-family: "Source Sans 3", sans-serif;
    font-size: 13px;
    color: var(--muted);
  }
  .contacts li {
    display: flex;
    align-items: center;
    gap: 7px;
    height: 30px;
  }
  .contacts svg { width: 10px; height: 10px; fill: var(--ink); flex: none; }

  .bands { position: absolute; left: 0; bottom: 0; width: 504px; height: 288px; }

  .services {
    position: absolute;
    left: 60px;
    right: 60px;
    top: 134px;
    text-align: center;
  }
  .services__title {
    font-family: "Montserrat", sans-serif;
    font-size: 10px;
    font-weight: 700;
    letter-spacing: 2px;
    color: var(--red);
    margin-bottom: 10px;
  }
  .services__list {
    list-style: none;
    display: flex;
    flex-wrap: wrap;
    justify-content: center;
    gap: 6px 14px;
    font-family: "Source Sans 3", sans-serif;
    font-size: 12px;
    color: var(--muted);
  }
  .services__list li { display: flex; align-items: center; gap: 5px; }
  .services__list li::before {
    content: "";
    width: 4px; height: 4px;
    background: var(--red);
  }
</style>
</head>
<body>
  <section class="card card--front">
    <div class="brand">
      <span class="brand__mark"></span>
      <span class="brand__name">VELKOR SERVICES INC.</span>
    </div>

    <div class="person">
      <p class="person__name">Daniel Marsh</p>
      <p class="person__role">Managing Member</p>
    </div>

    <div class="divider"></div>

    <ul class="contacts">
      <li>
        <svg viewBox="0 0 10 10"><path d="M2 0.5 L3.6 2.6 L2.7 3.6 C3.3 5 4.8 6.6 6.3 7.2 L7.3 6.2 L9.5 7.8 L8.3 9.5 C4.5 9.3 0.6 5.4 0.4 1.7 Z"/></svg>
        <span>0412-555-019</span>
      </li>
      <li>
        <svg viewBox="0 0 10 10"><path d="M0.5 2 H9.5 V8 H0.5 Z M1.2 2.6 L5 5.6 L8.8 2.6" stroke="#fff" stroke-width="0.7"/></svg>
        <span>@yourweb.com</span>
      </li>
      <li>
        <svg viewBox="0 0 10 10"><path d="M5 0.3 C2.8 0.3 1.4 1.9 1.4 3.8 C1.4 6.3 5 9.7 5 9.7 C5 9.7 8.6 6.3 8.6 3.8 C8.6 1.9 7.2 0.3 5 0.3 Z M5 2.4 A1.4 1.4 0 1 0 5 5.2 A1.4 1.4 0 1 0 5 2.4 Z" fill-rule="evenodd"/></svg>
        <span>your address here</span>
      </li>
    </ul>

    <svg class="bands" viewBox="0 0 504 288" aria-hidden="true">
      <polygon points="0,264.8 311,264.8 303,271 0,271" fill="var(--ink)"/>
      <polygon points="0,276 304,276 321,261 504,261 504,288 0,288" fill="var(--red)"/>
    </svg>
  </section>

  <section class="card card--back">
    <div class="brand">
      <span class="brand__mark"></span>
      <span class="brand__name">VELKOR SERVICES INC.</span>
    </div>

    <div class="services">
      <p class="services__title">TRUCKING INDUSTRY SERVICES</p>
      <ul class="services__list">
        <li>Safety Compliance</li>
        <li>Fleet Audits</li>
        <li>Permits &amp; Licensing</li>
        <li>Driver Training</li>
        <li>IFTA Reporting</li>
        <li>Operating Authority</li>
      </ul>
    </div>
  </section>
</body>
</html>
```